Create a business promotion flyer to leave in customer mailboxes. We are a bulk petroleum supplier, servicing any industry that requires diesel. Base in griffith NSW, servicing griffith area and surrounds.

Business Name - Terra Petro
Fuel@terrapetro-example.com.au
Marco - 0400 000 001 mtorrisi@terrapetro-example.com.au
Liam - 0400 000 002 lharcourt@terrapetro-example.com.au
Peter - 0400 000 003 pwinslow@terrapetro-example.com.au
Office 02 5550 0100

Bulk Fuel deliveries.
Oils & lubricants
Local Family owned business

```html
<!DOCTYPE html>
<html lang="en">
<head>
<meta charset="utf-8">
<title>Terra Petro – Bulk Fuel Flyer</title>
<link rel="stylesheet" href="https://fonts.googleapis.com/css2?family=Anton&family=Montserrat:ital,wght@0,500;0,600;0,700;0,800;1,800&display=swap">
<style>
  :root {
    --red: #e52b20;
    --ink: #2b2e31;
    --grey: #55585b;
    --rule: #c9c9c9;
    --white: #ffffff;
    --band: #2e3134;
    --sky-top: #8fb4dc;
    --sky-low: #dfe8f2;
    --yard: #c9c6c0;
  }
  * { box-sizing: border-box; margin: 0; padding: 0; }
  html, body { width: 731px; height: 1200px; overflow: hidden; background: var(--white); }
  body { font-family: "Montserrat", sans-serif; color: var(--ink); }

  .flyer { position: relative; width: 731px; height: 1200px; overflow: hidden; background: var(--white); }

  /* Header */
  .brand { position: absolute; left: 28px; top: 92px; width: 270px; display: flex; align-items: center; gap: 10px; }
  .brand-dot { width: 30px; height: 30px; border-radius: 50%; background: var(--red); flex: none; }
  .brand-name { font-family: "Montserrat", sans-serif; font-weight: 600; font-size: 38px; color: var(--red); letter-spacing: -0.5px; white-space: nowrap; }
  .header-rule { position: absolute; left: 310px; top: 22px; width: 2px; height: 225px; background: var(--red); }

  .headline { position: absolute; left: 336px; top: 20px; font-family: "Anton", sans-serif; font-size: 52px; line-height: 60px; color: var(--grey); letter-spacing: -0.5px; }
  .headline .accent { color: var(--red); }
  .service-area { position: absolute; left: 336px; top: 150px; background: var(--red); color: var(--white); font-weight: 700; font-size: 17.5px; padding: 2px 6px; letter-spacing: 0.3px; white-space: nowrap; }
  .intro { position: absolute; left: 336px; top: 192px; width: 380px; font-size: 12.5px; font-weight: 500; line-height: 17px; color: var(--ink); }

  /* Photo + swoosh */
  .hero-photo { position: absolute; left: 0; top: 240px; width: 731px; height: 372px;
    background: linear-gradient(180deg, var(--sky-top) 0%, var(--sky-low) 45%, #b9bcc0 62%, var(--yard) 100%); }
  .swoosh { position: absolute; left: 0; top: 540px; width: 731px; height: 270px; }

  /* Services */
  .services { position: absolute; left: 0; top: 742px; width: 731px; height: 232px; display: flex; }
  .service { position: relative; padding-top: 10px; }
  .service + .service::before { content: ""; position: absolute; left: 0; top: 0; width: 1px; height: 222px; background: var(--rule); }
  .service:nth-child(1) { width: 195px; padding-left: 46px; }
  .service:nth-child(2) { width: 159px; padding-left: 12px; }
  .service:nth-child(3) { width: 154px; padding-left: 11px; }
  .service:nth-child(4) { width: 223px; padding-left: 10px; }
  .service-icon { width: 76px; height: 76px; border-radius: 50%; background: var(--red); display: flex; align-items: center; justify-content: center; margin-left: 16px; }
  .service-icon svg { width: 46px; height: 46px; }
  .service-title { margin-top: 12px; font-weight: 800; font-size: 15.5px; line-height: 17px; text-transform: uppercase; color: var(--ink); }
  .service-title::after { content: ""; display: block; width: 60px; height: 3px; background: var(--red); margin-top: 2px; }
  .service-text { margin-top: 3px; font-size: 10.5px; font-weight: 600; line-height: 12px; color: var(--ink); }

  /* Contacts */
  .contacts { position: absolute; left: 0; top: 975px; width: 731px; height: 122px; background: var(--band); display: flex; padding-top: 26px; }
  .contact { position: relative; color: var(--white); }
  .contact + .contact::before { content: ""; position: absolute; left: 0; top: -4px; width: 1px; height: 70px; background: #7a7d80; }
  .contact:nth-child(1) { width: 242px; padding-left: 44px; }
  .contact:nth-child(2) { width: 236px; padding-left: 22px; }
  .contact:nth-child(3) { width: 253px; padding-left: 20px; }
  .contact-line { display: flex; align-items: center; gap: 10px; }
  .phone-badge { width: 32px; height: 32px; border-radius: 50%; background: var(--red); display: flex; align-items: center; justify-content: center; flex: none; }
  .phone-badge svg { width: 18px; height: 18px; }
  .contact-name { font-weight: 700; font-size: 15px; line-height: 18px; text-transform: uppercase; white-space: nowrap; }
  .contact-name span { display: block; text-transform: none; }
  .contact-mail { display: flex; align-items: center; gap: 12px; margin-top: 10px; margin-left: 10px; font-size: 8.6px; font-weight: 500; white-space: nowrap; }
  .contact-mail svg { width: 18px; height: 12px; flex: none; }

  /* Footer */
  .mail-bar { position: absolute; left: 0; top: 1100px; width: 731px; height: 45px; background: var(--red); color: var(--white); font-weight: 700; font-size: 22px; display: flex; align-items: center; justify-content: center; }
  .tagline { position: absolute; left: 0; top: 1146px; width: 731px; height: 54px; display: flex; align-items: center; justify-content: center; gap: 18px; }
  .tagline .line { width: 70px; height: 3px; background: var(--red); }
  .tagline p { font-weight: 800; font-style: italic; font-size: 16px; color: var(--red); word-spacing: 2px; white-space: nowrap; }
  .tagline p span + span { margin-left: 18px; }
</style>
</head>
<body>
<main class="flyer">

  <header>
    <div class="brand">
      <div class="brand-dot"></div>
      <div class="brand-name">Terra Petro</div>
    </div>
    <div class="header-rule"></div>
    <h1 class="headline">YOUR LOCAL<br><span class="accent">BULK FUEL</span> SUPPLIER</h1>
    <div class="service-area">SERVICING GRIFFITH &amp; SURROUNDS</div>
    <p class="intro">We supply high quality fuel and lubricants to keep your business and machinery running smoothly.</p>
  </header>

  <div class="hero-photo" role="img" aria-label="Photo of a white road-train fuel tanker parked outside a steel depot shed under a blue cloudy sky"></div>

  <svg class="swoosh" viewBox="0 0 731 270" preserveAspectRatio="none" aria-hidden="true">
    <path d="M0,54 C260,22 520,10 731,12 L731,26 C520,26 260,44 0,72 Z" fill="var(--white)"/>
    <path d="M0,72 C260,44 520,26 731,26 L731,122 C520,128 240,170 0,226 Z" fill="var(--red)"/>
    <path d="M0,226 C240,170 520,128 731,122 L731,270 L0,270 Z" fill="var(--white)"/>
    <path d="M0,240 C240,184 520,140 731,132" fill="none" stroke="var(--red)" stroke-width="3"/>
  </svg>

  <section class="services">
    <article class="service">
      <div class="service-icon">
        <svg viewBox="0 0 48 48" aria-hidden="true">
          <rect x="3" y="16" width="28" height="16" rx="8" fill="var(--white)"/>
          <path d="M32 20 h8 l5 6 v6 h-13 z" fill="var(--white)"/>
          <circle cx="10" cy="35" r="4" fill="var(--white)" stroke="var(--red)" stroke-width="2"/>
          <circle cx="22" cy="35" r="4" fill="var(--white)" stroke="var(--red)" stroke-width="2"/>
          <circle cx="39" cy="35" r="4" fill="var(--white)" stroke="var(--red)" stroke-width="2"/>
        </svg>
      </div>
      <h2 class="service-title">Bulk Fuel<br>Deliveries</h2>
      <p class="service-text">Reliable, on-time fuel delivered to your farm, site or business.</p>
    </article>
    <article class="service">
      <div class="service-icon">
        <svg viewBox="0 0 48 48" aria-hidden="true">
          <path d="M20 6 C20 6 8 22 8 30 a12 12 0 0 0 24 0 C32 22 20 6 20 6 Z" fill="var(--white)"/>
          <path d="M34 14 C34 14 28 22 28 26 a6 6 0 0 0 12 0 C40 22 34 14 34 14 Z" fill="var(--white)" stroke="var(--red)" stroke-width="2"/>
        </svg>
      </div>
      <h2 class="service-title">Oils &amp;<br>Lubricants</h2>
      <p class="service-text">Reliable, on-time fuel delivered to your farm, site or business.</p>
    </article>
    <article class="service">
      <div class="service-icon">
        <svg viewBox="0 0 48 48" aria-hidden="true">
          <path d="M14 8 h14 l4 6 v6 l-6 6 v8 h-12 z" fill="var(--white)"/>
          <path d="M14 34 l-6 8" stroke="var(--white)" stroke-width="5" stroke-linecap="round"/>
          <path d="M38 24 C38 24 33 31 33 34 a5 5 0 0 0 10 0 C43 31 38 24 38 24 Z" fill="var(--white)"/>
        </svg>
      </div>
      <h2 class="service-title">Petrol<br>Deliveries</h2>
      <p class="service-text">Reliable, on-time fuel delivered to your farm, site or business.</p>
    </article>
    <article class="service">
      <div class="service-icon">
        <svg viewBox="0 0 48 48" aria-hidden="true">
          <path d="M24 8 L42 23 h-5 v17 h-26 v-17 h-5 z" fill="var(--white)"/>
          <rect x="20" y="28" width="8" height="12" fill="var(--red)"/>
        </svg>
      </div>
      <h2 class="service-title">Local Family<br>Owned Business</h2>
      <p class="service-text">Reliable, on-time fuel<br>delivered to your farm,<br>site or business.</p>
    </article>
  </section>

  <section class="contacts">
    <div class="contact">
      <div class="contact-line">
        <div class="phone-badge"><svg viewBox="0 0 24 24" aria-hidden="true"><path d="M6.6 10.8a15 15 0 0 0 6.6 6.6l2.2-2.2a1 1 0 0 1 1-.25 11.4 11.4 0 0 0 3.6.57 1 1 0 0 1 1 1V20a1 1 0 0 1-1 1A17 17 0 0 1 3 4a1 1 0 0 1 1-1h3.5a1 1 0 0 1 1 1 11.4 11.4 0 0 0 .57 3.6 1 1 0 0 1-.25 1z" fill="var(--white)"/></svg></div>
        <div class="contact-name">Marco -<span>0400 000 001</span></div>
      </div>
      <div class="contact-mail"><svg viewBox="0 0 18 12" aria-hidden="true"><rect x="0.5" y="0.5" width="17" height="11" fill="none" stroke="var(--white)"/><path d="M0.5 0.5 L9 7 L17.5 0.5" fill="none" stroke="var(--white)"/></svg>Fuel@terrapetro-example.com.au</div>
    </div>
    <div class="contact">
      <div class="contact-line">
        <div class="phone-badge"><svg viewBox="0 0 24 24" aria-hidden="true"><path d="M6.6 10.8a15 15 0 0 0 6.6 6.6l2.2-2.2a1 1 0 0 1 1-.25 11.4 11.4 0 0 0 3.6.57 1 1 0 0 1 1 1V20a1 1 0 0 1-1 1A17 17 0 0 1 3 4a1 1 0 0 1 1-1h3.5a1 1 0 0 1 1 1 11.4 11.4 0 0 0 .57 3.6 1 1 0 0 1-.25 1z" fill="var(--white)"/></svg></div>
        <div class="contact-name">Liam -<span>0400 000 002</span></div>
      </div>
      <div class="contact-mail"><svg viewBox="0 0 18 12" aria-hidden="true"><rect x="0.5" y="0.5" width="17" height="11" fill="none" stroke="var(--white)"/><path d="M0.5 0.5 L9 7 L17.5 0.5" fill="none" stroke="var(--white)"/></svg>lharcourt@terrapetro-example.com.au</div>
    </div>
    <div class="contact">
      <div class="contact-line">
        <div class="phone-badge"><svg viewBox="0 0 24 24" aria-hidden="true"><path d="M6.6 10.8a15 15 0 0 0 6.6 6.6l2.2-2.2a1 1 0 0 1 1-.25 11.4 11.4 0 0 0 3.6.57 1 1 0 0 1 1 1V20a1 1 0 0 1-1 1A17 17 0 0 1 3 4a1 1 0 0 1 1-1h3.5a1 1 0 0 1 1 1 11.4 11.4 0 0 0 .57 3.6 1 1 0 0 1-.25 1z" fill="var(--white)"/></svg></div>
        <div class="contact-name">Peter -<span>0400 000 003</span></div>
      </div>
      <div class="contact-mail"><svg viewBox="0 0 18 12" aria-hidden="true"><rect x="0.5" y="0.5" width="17" height="11" fill="none" stroke="var(--white)"/><path d="M0.5 0.5 L9 7 L17.5 0.5" fill="none" stroke="var(--white)"/></svg>pwinslow@terrapetro-example.com.au</div>
    </div>
  </section>

  <div class="mail-bar">Fuel@terrapetro-example.com.au</div>

  <footer class="tagline">
    <div class="line"></div>
    <p><span>QUALITY FUEL.</span><span>RELIABLE SERVICE.</span><span>LOCAL PEOPLE</span></p>
    <div class="line"></div>
  </footer>

</main>
</body>
</html>
```